Etiketten-Design für Dankeswein
Zielgruppe
Vo-Lux:
Wir stellen für unsere Kunden einen Dankeswein her. Er soll eine Hommage an die Freundschaft und Partnerschaft sein.
Subtitle, could be, but perhaps not:
When we meet, anything can happen.
Name: Vo-Lux (evtl. Änderung auf KaFol)
Aufgabenstellung
Das Ettikett darf auch bunt sein, aber es sollte vorallem sehr Professionell sein.
Der Wein wird rötlich sein, die Flasche weiss durchsichtig. Es werden wahrscheinlich 0,5l Flaschen.
Die Form des Ettikets, kann noch definiert werden.
Es geht um eine Homage an das Treffen von Menschen und die Freundschaft.
Vo-Lux
Hintergrundinfos, die eher für den Hintergrund, Einarbeitung und kleine Abbildung gedacht sind.
TORVIK: ist eine IT Firma, die von 2 Partnern gegründet wurde. Das Logo sollte mit drauf, evtl. kann man auch sich an diesen Farben orientieren.
Familie Abegg: Die Tiersymbole repräsentieren die beiden Eltern. Das geschwungene H ist das Familienzeichen. Wenn man es rotiert. ähnelt es wieder einem Schmetterling. Vielleicht kann man da grafisch etwas machen?
Das geschwungene H oder die Tiersymbole haben hohen emotionalen Wert. In dem Wappen ist das neue Familiensymbol eingearbeitet in das noch ältere Familienwappen der Familie. Prio hat das geschwungene H
Für das Ettikett gibt es leider rechtliche Pflichtangaben:
TORVIK GmbH
Rindermarktgasse 9 CH-4052 Basel
Erzeugerab füllung:D- RP 7 438 926
A.P.-Nr.7 438 926 XXXX
11,0%vol 50 cl Enthält Sulfite
Deutscher Qualitätswein – Mosel
vo-lux.eu

```html
<!DOCTYPE html>
<html lang="de">
<head>
<meta charset="utf-8">
<title>Dankeswein Etiketten – KaFol &amp; Vo-Lux</title>
<link rel="stylesheet" href="https://fonts.googleapis.com/css2?family=Montserrat:wght@400;700;800&family=Roboto:wght@400&family=Roboto+Condensed:wght@400&display=swap">
<style>
  :root {
    --paper: #ffffff;
    --label-black: #000000;
    --gold: #c2ad5a;
    --gold-light: #ebdc9c;
    --year-blue: #1c9ad6;
    --rotling-green: #7ab51d;
    --brand-text: #9aa0a6;
    --band-red: #a10f28;
    --text-white: #ffffff;
  }
  * { box-sizing: border-box; margin: 0; padding: 0; }
  html, body {
    width: 848px; height: 1200px; overflow: hidden;
    background: var(--paper);
  }
  .canvas {
    position: relative; width: 848px; height: 1200px;
    display: flex; justify-content: center; align-items: center; gap: 68px;
  }
  .label {
    position: relative; width: 307px; height: 328px;
    background: var(--label-black); color: var(--text-white);
    text-align: center; overflow: hidden;
  }
  .label__brand {
    position: absolute; top: 16px; left: 0; right: 0;
    font-family: "Montserrat", sans-serif; font-weight: 400;
    font-size: 26px; letter-spacing: 1px; color: var(--brand-text);
  }
  .label__name {
    position: absolute; top: 58px; left: 0; right: 0;
    font-family: "Montserrat", sans-serif; font-weight: 800;
    font-size: 40px; line-height: 44px; letter-spacing: 0.5px;
    color: var(--gold); text-transform: uppercase;
  }
  .label__grapes {
    position: absolute; top: 102px; left: 50%; width: 64px; height: 90px;
    transform: translateX(-50%); border-radius: 32px 32px 40px 40px / 30px 30px 60px 60px;
    background: radial-gradient(circle at 40% 35%, var(--gold-light), var(--gold));
  }
  .label__vintage {
    position: absolute; top: 206px; left: 0; right: 0;
    font-family: "Montserrat", sans-serif; font-weight: 800;
    font-size: 17px; color: var(--year-blue);
  }
  .label__type {
    position: absolute; top: 227px; left: 0; right: 0;
    font-family: "Montserrat", sans-serif; font-weight: 700;
    font-size: 17px; letter-spacing: 1px; color: var(--rotling-green);
  }
  .label__quality {
    position: absolute; top: 255px; left: 0; right: 0;
    font-family: "Roboto", sans-serif; font-weight: 400;
    font-size: 12px; line-height: 15px; letter-spacing: 0.3px;
    padding-left: 0;
  }
  .label__family-mark {
    position: absolute; top: 266px; left: 10px; width: 57px; height: 30px;
    border-radius: 50%;
    background: linear-gradient(90deg, #3a3a3a, #6b6b6b);
  }
  .label__volume {
    position: absolute; top: 283px; left: 253px;
    font-family: "Roboto Condensed", sans-serif; font-size: 16px;
  }
  .label__legal {
    position: absolute; left: 0; right: 0; bottom: 0; height: 27px;
    background: var(--band-red);
    font-family: "Roboto Condensed", sans-serif; font-size: 7.6px; line-height: 11px;
    text-align: left; padding: 2px 8px 0 8px;
    display: flex; justify-content: space-between;
  }
  .label__legal-right { width: 50px; }
</style>
</head>
<body>
<main class="canvas">
  <article class="label">
    <div class="label__brand">TORVIK</div>
    <h1 class="label__name">KaFol</h1>
    <div class="label__grapes" role="img" aria-label="Goldene Weintrauben-Illustration"></div>
    <div class="label__vintage">2020</div>
    <div class="label__type">ROTLING</div>
    <div class="label__family-mark" role="img" aria-label="Geschwungenes Familienzeichen"></div>
    <p class="label__quality">DEUTSCHER QUALITÄTSWEIN<br>MOSEL</p>
    <div class="label__volume">50 cl</div>
    <div class="label__legal">
      <div>TORVIK GmbH, Rindermarktgasse 9 • CH-4052 Basel • vo-lux.eu<br>Erzeugerabfüllung: D-RP 7 438 926 • A.P.-Nr. 7 438 926 XXXX</div>
      <div class="label__legal-right">11,0% vol.<br>Enthält Sulfite</div>
    </div>
  </article>

  <article class="label">
    <div class="label__brand">TORVIK</div>
    <h1 class="label__name">Vo-Lux</h1>
    <div class="label__grapes" role="img" aria-label="Goldene Weintrauben-Illustration"></div>
    <div class="label__vintage">2020</div>
    <div class="label__type">ROTLING</div>
    <div class="label__family-mark" role="img" aria-label="Geschwungenes Familienzeichen"></div>
    <p class="label__quality">DEUTSCHER QUALITÄTSWEIN<br>MOSEL</p>
    <div class="label__volume">50 cl</div>
    <div class="label__legal">
      <div>TORVIK GmbH, Rindermarktgasse 9 • CH-4052 Basel • vo-lux.eu<br>Erzeugerabfüllung: D-RP 7 438 926 • A.P.-Nr. 7 438 926 XXXX</div>
      <div class="label__legal-right">11,0% vol.<br>Enthält Sulfite</div>
    </div>
  </article>
</main>
</body>
</html>
```